Radio Service company needs ad for trade publication

Airwave Partners provides sales, content, production, technology, and promotion products and services to radio stations to help increase sales and solutions to improve operations and reduce costs. We are looking for a creative ad (sizes 720x250, 300x250, 728x180) with a theme around "MASTER YOUR 2024 BUDGET with AIRWAVE PARTNERS". Categories we have products/services to help them get budget into alignment. (1) Sales (2) Content & Programming (3) Technology (4) Production & Imaging (5) Promotions & Marketing (6) Support Services
"Don't go into the new year with an Unrealistic Budget.....We can Help!"

```html
<!DOCTYPE html>
<html lang="en">
<head>
<meta charset="utf-8">
<title>Airwave Partners – Balance Your 2024 Budget Ads</title>
<link rel="stylesheet" href="https://fonts.googleapis.com/css2?family=Anton&family=Poppins:wght@500;600;700;800&display=swap">
<style>
  :root {
    --stage: #0f9bf2;
    --navy-deep: #1d2f86;
    --navy: #2a44a8;
    --navy-light: #3957c4;
    --white: #ffffff;
    --sky: #1aa3f5;
    --yellow: #fbc02d;
    --ink: #12154a;
    --divider: rgba(255,255,255,0.85);
  }
  * { box-sizing: border-box; margin: 0; padding: 0; }
  html, body { width: 1200px; height: 1200px; overflow: hidden; }
  body { background: var(--stage); position: relative; font-family: "Poppins", sans-serif; }

  .ad {
    position: absolute;
    overflow: hidden;
    background: linear-gradient(120deg, var(--navy-deep) 0%, var(--navy) 55%, var(--navy-light) 100%);
    box-shadow: 0 4px 14px rgba(0,0,0,0.25);
  }
  .ad--wide { left: 60px; top: 27px; width: 1080px; height: 375px; }
  .ad--leader { left: 54px; top: 442px; width: 1092px; height: 270px; }
  .ad--square { left: 60px; top: 754px; width: 504px; height: 420px; }

  .headline { position: absolute; color: var(--white); font-family: "Anton", sans-serif; text-transform: uppercase; line-height: 1; }
  .headline span { display: block; position: absolute; left: 0; white-space: nowrap; }
  .headline .with-tag {
    font-family: "Poppins", sans-serif; font-weight: 800; background: var(--sky);
    color: var(--ink); padding: 0 6px; line-height: 1.25; z-index: 2;
  }

  .divider { position: absolute; width: 3px; background: var(--divider); }

  .solutions { position: absolute; color: var(--white); }
  .solutions h2 { font-weight: 700; text-transform: uppercase; letter-spacing: 0.2px; line-height: 1.2; }
  .solutions ul { list-style: none; }
  .solutions li { position: relative; padding-left: 26px; font-weight: 500; line-height: 1.2; white-space: nowrap; }
  .solutions li::before {
    content: ""; position: absolute; left: 2px; top: 50%; transform: translateY(-50%);
    border-left: 13px solid var(--sky); border-top: 9px solid transparent; border-bottom: 9px solid transparent;
  }

  .offer {
    position: absolute; background: var(--yellow); color: var(--white);
    text-align: center; font-weight: 500; line-height: 1.25; padding: 6px 10px;
  }
  .offer strong { font-weight: 800; }
  .offer .offer-cta { display: block; color: var(--ink); font-weight: 800; text-transform: uppercase; margin-top: 2px; }

  .scale-art {
    position: absolute; border-radius: 10px;
    background: linear-gradient(180deg, rgba(120,170,240,0.35) 0%, rgba(26,163,245,0.25) 60%, rgba(255,255,255,0.15) 100%);
  }

  .brand-corner {
    position: absolute; background: var(--white); border-radius: 0 0 0 100%;
    display: flex; align-items: center; justify-content: flex-end;
  }
  .brand-name {
    font-family: "Poppins", sans-serif; font-weight: 700; color: var(--sky);
    text-transform: uppercase; line-height: 1.05; text-align: center;
  }

  /* wide 720x250 */
  .ad--wide .headline { left: 20px; top: 0; width: 320px; height: 375px; }
  .ad--wide .hl-1 { top: 68px; font-size: 72px; }
  .ad--wide .hl-2 { top: 146px; font-size: 33px; }
  .ad--wide .with-tag { left: 178px !important; top: 180px; font-size: 17px; }
  .ad--wide .hl-3 { top: 196px; font-size: 76px; }
  .ad--wide .hl-4 { top: 290px; font-size: 54px; }
  .ad--wide .divider { left: 337px; top: 96px; height: 208px; }
  .ad--wide .solutions { left: 360px; top: 88px; }
  .ad--wide .solutions h2 { font-size: 22px; margin-bottom: 10px; }
  .ad--wide .solutions li { font-size: 20px; margin-bottom: 8px; }
  .ad--wide .offer { left: 360px; top: 225px; width: 447px; height: 77px; font-size: 17px; }
  .ad--wide .offer-cta { font-size: 19px; }
  .ad--wide .scale-art { left: 830px; top: 135px; width: 225px; height: 237px; }
  .ad--wide .brand-corner { left: 855px; top: 0; width: 225px; height: 88px; padding-right: 22px; }
  .ad--wide .brand-name { font-size: 21px; }

  /* leaderboard 728x180 */
  .ad--leader .headline { left: 15px; top: 0; width: 310px; height: 270px; }
  .ad--leader .hl-1 { top: 14px; font-size: 66px; }
  .ad--leader .hl-2 { top: 86px; font-size: 31px; }
  .ad--leader .with-tag { left: 120px !important; top: 118px; font-size: 17px; }
  .ad--leader .hl-3 { top: 124px; font-size: 72px; }
  .ad--leader .hl-4 { top: 207px; font-size: 50px; }
  .ad--leader .divider { left: 328px; top: 36px; height: 200px; }
  .ad--leader .solutions { left: 342px; top: 22px; }
  .ad--leader .solutions h2 { font-size: 21px; margin-bottom: 8px; }
  .ad--leader .solutions li { font-size: 20px; margin-bottom: 8px; }
  .ad--leader .offer { left: 348px; top: 165px; width: 460px; height: 76px; font-size: 17px; }
  .ad--leader .offer-cta { font-size: 19px; }
  .ad--leader .scale-art { left: 820px; top: 70px; width: 195px; height: 195px; }
  .ad--leader .brand-corner { left: 852px; top: 0; width: 240px; height: 128px; padding-right: 22px; }
  .ad--leader .brand-name { font-size: 22px; }

  /* square 336x280 */
  .ad--square .headline { left: 22px; top: 0; width: 280px; height: 280px; }
  .ad--square .hl-1 { top: 30px; font-size: 62px; }
  .ad--square .hl-2 { top: 97px; font-size: 28px; }
  .ad--square .with-tag { left: 108px !important; top: 127px; font-size: 15px; }
  .ad--square .hl-3 { top: 134px; font-size: 70px; }
  .ad--square .hl-4 { top: 216px; font-size: 44px; }
  .ad--square .scale-art { left: 292px; top: 102px; width: 195px; height: 162px; }
  .ad--square .brand-corner { left: 285px; top: 0; width: 219px; height: 93px; padding-right: 18px; }
  .ad--square .brand-name { font-size: 19px; }
  .ad--square .solutions { left: 24px; top: 268px; }
  .ad--square .solutions h2 { font-size: 22px; margin-bottom: 10px; }
  .ad--square .solutions li { font-size: 20px; margin-bottom: 8px; }
</style>
</head>
<body>

  <section class="ad ad--wide" aria-label="Airwave Partners ad, 720 by 250">
    <h1 class="headline">
      <span class="hl-1">Balance</span>
      <span class="hl-2">Your 2024 Budget</span>
      <span class="with-tag">WITH</span>
      <span class="hl-3">Airwave</span>
      <span class="hl-4">Partners</span>
    </h1>
    <div class="divider"></div>
    <div class="solutions">
      <h2>Solutions for Broadcasters</h2>
      <ul>
        <li>Need to Improve Your Cash Flow?</li>
        <li>Need to Streamline Your Expenses?</li>
        <li>Need more Non-Traditional Revenue?</li>
      </ul>
    </div>
    <p class="offer"><strong>START SAVINGS NOW!</strong> Packages are available with no payments until year 2025<span class="offer-cta">Click here to contact us today!</span></p>
    <div class="scale-art" role="img" aria-label="Balance scale weighing a green revenue box against a red expenses box"></div>
    <div class="brand-corner"><p class="brand-name">Airwave<br>Partners</p></div>
  </section>

  <section class="ad ad--leader" aria-label="Airwave Partners ad, 728 by 180">
    <h1 class="headline">
      <span class="hl-1">Balance</span>
      <span class="hl-2">Your 2024 Budget</span>
      <span class="with-tag">WITH</span>
      <span class="hl-3">Airwave</span>
      <span class="hl-4">Partners</span>
    </h1>
    <div class="divider"></div>
    <div class="solutions">
      <h2>Solutions for Broadcasters</h2>
      <ul>
        <li>Need to Improve Your Cash Flow?</li>
        <li>Need to Streamline Your Expenses?</li>
        <li>Need more Non-Traditional Revenue?</li>
      </ul>
    </div>
    <p class="offer"><strong>START SAVINGS NOW!</strong> Packages are available with no payments until year 2025<span class="offer-cta">Click here to contact us today!</span></p>
    <div class="scale-art" role="img" aria-label="Balance scale weighing a green revenue box against a red expenses box"></div>
    <div class="brand-corner"><p class="brand-name">Airwave<br>Partners</p></div>
  </section>

  <section class="ad ad--square" aria-label="Airwave Partners ad, 336 by 280">
    <h1 class="headline">
      <span class="hl-1">Balance</span>
      <span class="hl-2">Your 2024 Budget</span>
      <span class="with-tag">WITH</span>
      <span class="hl-3">Airwave</span>
      <span class="hl-4">Partners</span>
    </h1>
    <div class="scale-art" role="img" aria-label="Balance scale weighing a green revenue box against a red expenses box"></div>
    <div class="brand-corner"><p class="brand-name">Airwave<br>Partners</p></div>
    <div class="solutions">
      <h2>Solutions for Broadcasters</h2>
      <ul>
        <li>Need to Improve Your Cash Flow?</li>
        <li>Need to Streamline Your Expenses?</li>
        <li>Need more Non-Traditional Revenue?</li>
      </ul>
    </div>
  </section>

</body>
</html>
```